Web design for a crypto donation landing page for wildlife protection projects

We are developing the landing page for the presale of a web3 project, which will collect cryptos to send them to wildlife protection projects.
Here some website we like:
https://www.tinyshareforcanopy.fr/
https://vorlq.io/
https://www.bramwild.io/
please, use the wireframe to know what blocks we want but we accept different template.
If possible, do the design on figma. Use 1 or 2 fonts max. Used green, blue and white, no more. Make a consistent system design by using the same font size for H1, H2, H3... and the same colors everywhere.
Number of Pages Required
1 page
Look and feel
Each slider illustrates characteristics of the customer's brand and the style your logo design should communicate.

```html
<!DOCTYPE html>
<html lang="fr">
<head>
<meta charset="utf-8">
<title>ElanVert – Protégeons la nature ensemble</title>
<link href="https://fonts.googleapis.com/css2?family=Lexend:wght@400;500;600&family=Questrial&display=swap" rel="stylesheet">
<style>
:root{
  --purple:#2c1888;
  --green:#6cc01e;
  --green-dark:#4b8f14;
  --ink:#1d1b3a;
  --grey:#55556a;
  --white:#ffffff;
  --line:#d9d9e3;
}
*{margin:0;padding:0;box-sizing:border-box}
html,body{width:1200px;height:4413px;overflow:hidden;background:var(--white)}
body{position:relative;font-family:"Questrial",sans-serif;color:var(--ink)}
.abs{position:absolute}
h1,h2,h3{font-family:"Lexend",sans-serif;font-weight:500}

/* header */
.brand-tab{left:0;top:0;width:338px;height:86px;background:var(--purple);border-bottom-right-radius:86px;z-index:3}
.brand-tab .brand{position:absolute;left:108px;top:46px}
.brand{display:flex;align-items:center;gap:8px;color:var(--white);font-family:"Lexend",sans-serif;font-weight:500;font-size:16px}
.brand .dot{width:22px;height:22px;border-radius:50%;background:var(--green)}

/* hero */
.hero-bg{left:0;top:0;width:1200px;height:700px;background:linear-gradient(90deg,#ffffff 0%,#f3f3f4 40%,#dcdcdc 70%,#cfcbc2 100%)}
.hero-title{left:108px;top:200px;font-size:33px;letter-spacing:3px}
.hero-title em{font-style:normal;color:var(--green-dark)}
.hero-sub{left:108px;top:250px;font-size:15px;font-weight:600;font-family:"Lexend",sans-serif}
.hero-text{left:108px;top:305px;width:480px;font-size:16px;line-height:25px;color:var(--grey)}
.partner{top:494px;height:26px;border-radius:13px;background:#c9c9d6}

/* ocean */
.ocean{left:0;top:650px;width:1200px;height:860px;background:linear-gradient(180deg,#9fc2c2 0%,#8fb8b5 40%,#7ea29a 75%,#8a9f8f 100%)}

/* buy bar */
.buy{left:108px;top:591px;width:984px;height:120px;background:var(--white);border-radius:14px;box-shadow:0 8px 24px rgba(0,0,0,.12);z-index:4}
.buy h3{position:absolute;left:44px;top:43px;font-size:29px;letter-spacing:1px;color:#1f5a32;font-weight:400}
.counter{position:absolute;left:379px;top:40px;width:197px;height:41px;border:2px solid #7a7a90;border-radius:21px;display:flex;justify-content:space-around;align-items:center;font-family:"Lexend",sans-serif;font-size:27px}
.counter span:first-child,.counter span:last-child{font-size:24px}
.rate{position:absolute;left:608px;top:52px;font-size:14px;color:#888}
.buy-btn{position:absolute;left:749px;top:40px;width:197px;height:41px;border-radius:21px;background:linear-gradient(90deg,#8fd62a,#2f9a24);color:var(--white);font-size:13px;font-family:"Lexend",sans-serif;display:flex;align-items:center;justify-content:center;letter-spacing:1px}

.section-title{left:0;width:1200px;text-align:center;font-size:33px;letter-spacing:1.5px;line-height:40px}

/* cards */
.card{top:980px;width:301px;height:302px;background:var(--purple);border-radius:14px;color:var(--white);padding:36px 23px}
.card .icon{width:44px;height:44px;border:2px solid var(--green);border-radius:50%;margin-bottom:24px}
.card h3{font-size:14px;line-height:23px;font-weight:600;letter-spacing:.5px;text-transform:uppercase;margin-bottom:14px}
.card p{font-size:13px;line-height:21.5px;color:#d9d4f5}

/* community */
.com-title{left:108px;top:1572px;width:700px;font-size:33px;line-height:40px;letter-spacing:1px}
.com-sub{left:108px;top:1679px;width:690px;font-family:"Lexend",sans-serif;font-size:15px;line-height:25px;color:var(--grey)}
.social{top:1746px;display:flex;align-items:center;gap:14px;font-size:17px;color:var(--grey)}
.social .ico{width:40px;height:40px;border-radius:50%;background:#111}
.com-lead{left:108px;top:1823px;font-size:17px;color:var(--grey)}
.checks{left:122px;top:1866px;width:620px;list-style:none}
.checks li{display:flex;gap:20px;font-size:17px;line-height:19px;color:var(--grey);margin-bottom:18px}
.checks li svg{flex:none;margin-top:2px}
.com-photo{left:852px;top:1586px;width:446px;height:446px;border-radius:50%;background:#8a7a6c}

/* roadmap */
.dark-band{left:0;top:2151px;width:1200px;height:940px;background:linear-gradient(180deg,#0f2820 0%,#14302a 45%,#5a3a34 72%,#ffffff 100%)}
.roadmap{left:113px;top:2067px;width:977px;height:612px;background:var(--purple);border-radius:14px;overflow:hidden;color:var(--white)}
.roadmap h2{position:absolute;top:45px;width:100%;text-align:center;font-size:31px;letter-spacing:3px}
.roadmap .arrows{position:absolute;left:452px;top:92px}
.timeline{position:absolute;left:0;top:328px;width:100%;height:3px;background:var(--green)}
.node{position:absolute;width:24px;height:24px;border-radius:50%;background:var(--green)}
.vline{position:absolute;width:2px;background:var(--green)}
.q{position:absolute;font-family:"Lexend",sans-serif;font-size:19px;letter-spacing:1.5px}
.tasks{position:absolute;list-style:none;font-size:12.5px;line-height:27px;white-space:nowrap;color:#e6e2fb}
.tasks li::before{content:"• "}

/* faq */
.faq{left:158px;top:3095px;width:882px}
.faq-item{border-bottom:1px solid var(--line);padding:12px 16px;display:flex;justify-content:space-between;align-items:center;font-family:"Lexend",sans-serif;font-size:13px;height:46px}
.faq-open{height:auto;flex-wrap:wrap;padding-bottom:14px}
.faq-open p{width:100%;padding:16px 26px 0;font-family:"Questrial",sans-serif;font-size:12.5px;line-height:24px;color:var(--grey)}

/* team */
.team-bg{left:0;top:3480px;width:1200px;height:620px;background:linear-gradient(180deg,#ffffff 0%,#f2f6f9 40%,#e7ecf4 100%)}
.member{top:3656px;width:191px}
.member .photo{width:191px;height:221px;border-radius:6px;background:#ececef}
.member h3{margin-top:20px;font-size:16px;line-height:20px;font-weight:500}
.member p{margin-top:10px;font-size:13px;line-height:20px;color:var(--grey)}

/* footer */
.footer-txt{color:var(--white);font-size:16px;line-height:21px;font-family:"Lexend",sans-serif;font-weight:400}
.footer-brand{left:108px;top:4183px;display:flex;flex-direction:column;align-items:flex-start;gap:12px}
.footer-brand .dot{width:60px;height:60px;border-radius:50%;background:var(--green);margin-left:60px}
.footer-brand span{font-family:"Lexend",sans-serif;font-size:26px;color:var(--white);font-weight:500}
.contact-btn{left:866px;top:4196px;width:224px;height:41px;border:2px solid var(--white);border-radius:21px;display:flex;align-items:center;justify-content:center;color:var(--white);font-family:"Lexend",sans-serif;font-size:14px;letter-spacing:1px;font-weight:600}
.foot-social{left:924px;top:4310px;display:flex;gap:24px}
.foot-social span{width:20px;height:20px;border-radius:50%;background:var(--white)}
.copy{left:0;top:4398px;width:1200px;text-align:center;font-size:13px;color:#8a80c8}
</style>
</head>
<body>

<div class="abs hero-bg" role="img" aria-label="Ours polaire debout sur la banquise enneigée"></div>
<div class="abs ocean" role="img" aria-label="Fond marin avec rochers et eau turquoise"></div>
<svg class="abs" style="left:0;top:1330px" width="1200" height="180" viewBox="0 0 1200 180" aria-hidden="true">
  <path d="M0 180V150C250 160 380 60 640 70S1000 10 1200 30V180Z" fill="#ffffff"/>
</svg>

<header class="abs brand-tab">
  <div class="brand"><span class="dot"></span>ElanVert</div>
</header>

<h1 class="abs hero-title">Protégeons la <em>nature</em> ensemble</h1>
<p class="abs hero-sub">Faites un don de tokens et aidez à protéger la faune et flore.</p>
<p class="abs hero-text">Notre plateforme vous permet d'ajouter des tokens dev otre choix pour les donner a un projet de protectiond e la nature. Votre contribution aidera à financer des actions concrètes pour préserver l'environnement.</p>
<div class="abs partner" style="left:111px;width:86px"></div>
<div class="abs partner" style="left:245px;width:128px"></div>
<div class="abs partner" style="left:415px;width:128px"></div>

<section class="abs buy">
  <h3>ACHETER DES TOKEN</h3>
  <div class="counter"><span>-</span><span>12</span><span>+</span></div>
  <div class="rate">12 token = €30</div>
  <div class="buy-btn">ACHETER</div>
</section>

<h2 class="abs section-title" style="top:838px">Comment protéger la nature avec<br>des tokens Élan Vert?</h2>

<article class="abs card" style="left:110px">
  <div class="icon"></div>
  <h3>Achetez des tokens<br>Élan Vert</h3>
  <p>Les tokens sont des actifs numériques qui peuvent être utilisés pour financer des projets des associations.</p>
</article>
<article class="abs card" style="left:451px">
  <div class="icon"></div>
  <h3>Votez pour un<br>projet</h3>
  <p>Vous pouvez voter pour un projet de votre choix. Les projets sont proposés par des associations et des ONG qui travaillent pour la</p>
</article>
<article class="abs card" style="left:792px">
  <div class="icon"></div>
  <h3>L'association choisit<br>reçoit l'argent</h3>
  <p>Le projet qui a reçu le plus de votes recevra les tokens. L'association pourra utiliser cet argent pour financer ses actions concrètes pour protéger la nature.</p>
</article>

<h2 class="abs com-title">Rejoignez la communauté pour soutenir la protection de la nature</h2>
<p class="abs com-sub">La nature est en danger, nous devons agir ensemble. Rejoignez la communaute pour soutenir la protection de la nature.</p>
<div class="abs social" style="left:108px"><span class="ico"></span>Parloir</div>
<div class="abs social" style="left:256px"><span class="ico"></span>Chirp</div>
<p class="abs com-lead">En rejoignant la communaute, vous pourrez:</p>
<ul class="abs checks">
  <li><svg width="22" height="22" viewBox="0 0 22 22"><circle cx="11" cy="11" r="11" fill="#3aa335"/><path d="M6 11.5l3.2 3L16 7.8" stroke="#fff" stroke-width="2.4" fill="none"/></svg>Suivre les projets des associations qui travaillent pour la protection de la nature.</li>
  <li><svg width="22" height="22" viewBox="0 0 22 22"><circle cx="11" cy="11" r="11" fill="#3aa335"/><path d="M6 11.5l3.2 3L16 7.8" stroke="#fff" stroke-width="2.4" fill="none"/></svg>Voter pour le projet de votre choix et aider à financer ses actions concretes.</li>
  <li><svg width="22" height="22" viewBox="0 0 22 22"><circle cx="11" cy="11" r="11" fill="#3aa335"/><path d="M6 11.5l3.2 3L16 7.8" stroke="#fff" stroke-width="2.4" fill="none"/></svg>Etre informé des dernières actualités sur la protection de la nature.</li>
</ul>
<div class="abs com-photo" role="img" aria-label="Mains tenant un caneton"></div>

<div class="abs dark-band" role="img" aria-label="Forêt sombre puis oiseau rouge posé sur des fleurs rouges"></div>

<section class="abs roadmap">
  <h2>ROADMAP</h2>
  <svg class="arrows" width="74" height="20" viewBox="0 0 74 20" aria-hidden="true">
    <path d="M30 10H4M11 3L4 10l7 7M44 10h26M63 3l7 7-7 7" stroke="#fff" stroke-width="2" fill="none"/>
  </svg>
  <div class="timeline"></div>

  <div class="vline" style="left:102px;top:160px;height:170px"></div>
  <div class="node" style="left:91px;top:318px"></div>
  <ul class="tasks" style="left:118px;top:156px">
    <li>Site internet &amp; reseaux sociaux</li>
    <li>Marketing &amp; development du smart contract tesnet</li>
    <li>Juridique et Pre vente n'l</li>
    <li>Developpment du smart contract tesnet</li>
  </ul>
  <div class="q" style="left:91px;top:356px">Q1 2024</div>

  <div class="vline" style="left:373px;top:330px;height:168px"></div>
  <div class="node" style="left:362px;top:318px"></div>
  <div class="q" style="left:362px;top:283px">Q2 2024</div>
  <ul class="tasks" style="left:386px;top:418px">
    <li>Site internet &amp; reseaux sociaux</li>
    <li>Marketing &amp; development du</li>
    <li>&nbsp;&nbsp;smart contract tesnet</li>
  </ul>

  <div class="vline" style="left:633px;top:160px;height:170px"></div>
  <div class="node" style="left:622px;top:318px"></div>
  <ul class="tasks" style="left:651px;top:156px">
    <li>Site internet &amp; reseaux sociaux</li>
    <li>Marketing &amp; development du smart contract tesnet</li>
    <li>Juridique et Pre vente n'l</li>
    <li>Developpment du smart contract tesnet</li>
  </ul>
  <div class="q" style="left:621px;top:356px">Q3 2024</div>

  <div class="vline" style="left:873px;top:330px;height:168px"></div>
  <div class="node" style="left:862px;top:318px"></div>
  <div class="q" style="left:864px;top:283px">Q4 2024</div>
  <ul class="tasks" style="left:898px;top:392px">
    <li>Site internet &amp; reseaux sociaux</li>
    <li>Marketing &amp; development du</li>
    <li>&nbsp;&nbsp;smart contract tesnet</li>
  </ul>
</section>

<h2 class="abs section-title" style="top:3022px">Frequently Asked Questions</h2>
<div class="abs faq">
  <div class="faq-item faq-open">Frequently Asked Question 1
    <svg width="16" height="10" viewBox="0 0 16 10"><path d="M2 8l6-6 6 6" stroke="#1d1b3a" stroke-width="2.4" fill="none"/></svg>
    <p>Lorem ipsum dolor sit amet, consectetur adipiscing elit, sed do eiusmod tempor incididunt ut labore et dolore magna aliqua. Quis ipsum suspendisse ultrices gravida maecenas, accumsan lacus vel facilisis.</p>
  </div>
  <div class="faq-item">Frequently Asked Question 2<svg width="16" height="10" viewBox="0 0 16 10"><path d="M2 2l6 6 6-6" stroke="#1d1b3a" stroke-width="2.4" fill="none"/></svg></div>
  <div class="faq-item">Frequently Asked Question 3<svg width="16" height="10" viewBox="0 0 16 10"><path d="M2 2l6 6 6-6" stroke="#1d1b3a" stroke-width="2.4" fill="none"/></svg></div>
  <div class="faq-item">Frequently Asked Question 4<svg width="16" height="10" viewBox="0 0 16 10"><path d="M2 2l6 6 6-6" stroke="#1d1b3a" stroke-width="2.4" fill="none"/></svg></div>
  <div class="faq-item">Frequently Asked Question 5<svg width="16" height="10" viewBox="0 0 16 10"><path d="M2 2l6 6 6-6" stroke="#1d1b3a" stroke-width="2.4" fill="none"/></svg></div>
  <div class="faq-item">Frequently Asked Question 6<svg width="16" height="10" viewBox="0 0 16 10"><path d="M2 2l6 6 6-6" stroke="#1d1b3a" stroke-width="2.4" fill="none"/></svg></div>
</div>

<div class="abs team-bg"></div>
<h2 class="abs section-title" style="top:3590px">Meet The Team</h2>
<div class="abs member" style="left:207px">
  <div class="photo" role="img" aria-label="Portrait de Julien Marchetti"></div>
  <h3>Marchetti<br>Julien</h3><p>Fondateur</p>
</div>
<div class="abs member" style="left:506px">
  <div class="photo" role="img" aria-label="Portrait de Sophie Lemaire"></div>
  <h3>Lemaire<br>Sophie</h3><p>Developpeuse<br>blockchain</p>
</div>
<div class="abs member" style="left:804px">
  <div class="photo" role="img" aria-label="Portrait d'Amandine Duval"></div>
  <h3>Duval<br>Amandine</h3><p>Developpeur front-end</p>
</div>

<svg class="abs" style="left:0;top:3990px" width="1200" height="423" viewBox="0 0 1200 423" aria-hidden="true">
  <path d="M0 60C200 120 420 10 700 40S1050 20 1200 0V423H0Z" fill="#2c1888"/>
</svg>
<div class="abs footer-brand"><span class="dot"></span><span>ElanVert</span></div>
<p class="abs footer-txt" style="left:370px;top:4188px">14 Rue Verdier<br>Paris 3C</p>
<p class="abs footer-txt" style="left:370px;top:4254px">+33 412 000 781<br>info@elanvert.com</p>
<p class="abs footer-txt" style="left:370px;top:4314px">Terms &amp; Conditions</p>
<div class="abs contact-btn">CONTACT US</div>
<div class="abs foot-social"><span></span><span></span><span></span></div>
<p class="abs copy">www.elanvert.com</p>

</body>
</html>
```